'Cradle Ahead' promotional brochure

We have designed a 6 week program to educate impending first-time parents about the things they need to know to survive the first 6 months. Sessions delivered by general practitioner/family doctor, dietician, physiotherapist, speech pathologist and psychologist. Our promotional blurb is: 'A comprehensive education program for first-time parents-to-be, delivered over 6 weeks by health professionals in your community, about everything you need to know to look after your baby (and yourself!) in the first 6 months'. I now want to put together a promotional brochure to be distributed to those couples who express an interest which will provide further details of what will be delivered in the course.
Updates
In terms of layout, I envisaged a double sided A4 size, foldable into 3 sections, but very happy to be guided on this.
Target Market(s)
To appeal to a young, well educated demographic. First time parents couples.
Industry/Entity Type
Medical
Font styles to use
Other font styles liked:
- Playfair Display
Requirements
Must have
- Playfair display font to be consistent with our logo (attached). Logo also included please. Some consistency with colours of logo please.
Nice to have
- I am a doctor, and have no creative genes! But prefer a clean and professional appearance overall. Not too cluttered in overall appearance.
Should not have
- No cheesy pictures of babies.

```html
<!DOCTYPE html>
<html lang="en">
<head>
<meta charset="utf-8">
<title>Cradle Ahead – Program Flyer</title>
<link rel="stylesheet" href="https://fonts.googleapis.com/css2?family=Lato:wght@300;400;700;900&family=Playfair+Display:wght@400&display=swap">
<style>
  :root {
    --green: #6cc13a;
    --green-dark: #5aab2c;
    --ink: #3c3c3c;
    --grey-panel: #e6e6e6;
    --paper: #ffffff;
    --backdrop: #d9d9d9;
    --photo-a: #f2d4bf;
    --photo-b: #b9876a;
  }
  * { box-sizing: border-box; margin: 0; padding: 0; }
  html, body { width: 1200px; height: 1200px; overflow: hidden; background: var(--backdrop); }
  .flyer {
    position: absolute; left: 186px; top: 20px;
    width: 827px; height: 1160px;
    background: var(--paper); overflow: hidden;
    font-family: "Lato", sans-serif; color: var(--ink);
    box-shadow: 0 4px 18px rgba(0,0,0,.18);
  }
  .grey-panel { position: absolute; left: 390px; top: 340px; right: 0; bottom: 0; background: var(--grey-panel); }
  .shapes { position: absolute; inset: 0; }
  .brand { position: absolute; left: 48px; top: 40px; display: flex; align-items: center; gap: 14px; }
  .brand-mark { width: 58px; height: 58px; border-radius: 50%; background: var(--green); }
  .brand-name { font-family: "Playfair Display", serif; font-weight: 400; font-size: 19px; line-height: 21px; color: var(--ink); letter-spacing: .5px; text-transform: uppercase; }
  .title { position: absolute; left: 68px; top: 135px; line-height: 1; }
  .title-light { display: block; font-weight: 300; font-size: 56px; color: #555; }
  .title-bold { display: block; font-weight: 900; font-size: 80px; color: var(--green); margin-top: 2px; }
  .cost { position: absolute; left: 70px; top: 285px; font-size: 17px; }
  .tab {
    position: absolute; height: 46px; background: var(--green); color: #fff;
    font-weight: 900; font-size: 31px; line-height: 46px; letter-spacing: .5px;
  }
  .tab-left { left: 0; padding: 0 22px 0 26px; border-radius: 0 18px 18px 0; }
  .tab-right { right: 0; padding: 0 28px 0 22px; border-radius: 18px 0 0 18px; }
  .copy { position: absolute; font-size: 13px; line-height: 16.3px; }
  .copy p + p { margin-top: 16px; }
  .justify { text-align: justify; hyphens: auto; }
  .right { text-align: right; }
  .topics { list-style: none; }
  .topics li { position: relative; padding-left: 12px; }
  .topics li::before { content: ""; position: absolute; left: 0; top: 6px; width: 5px; height: 5px; border-radius: 50%; background: var(--green); }
  .topics.align-right li { padding-left: 0; padding-right: 10px; }
  .topics.align-right li::before { left: auto; right: 0; }
  .contact { position: absolute; right: 40px; top: 1052px; color: #fff; font-size: 13.5px; line-height: 17.5px; text-align: right; }
  .contact-line { display: flex; justify-content: flex-end; align-items: center; gap: 8px; }
  .contact-line svg { width: 11px; height: 11px; flex: none; }
  .contact-line.no-icon { padding-right: 19px; }
</style>
</head>
<body>
<main class="flyer">
  <div class="grey-panel"></div>

  <svg class="shapes" viewBox="0 0 827 1160" width="827" height="1160" aria-hidden="false">
    <defs>
      <radialGradient id="photoTone" cx="60%" cy="40%" r="70%">
        <stop offset="0" stop-color="var(--photo-a)"/>
        <stop offset="1" stop-color="var(--photo-b)"/>
      </radialGradient>
    </defs>
    <circle cx="705" cy="80" r="402" fill="var(--green)"/>
    <circle cx="700" cy="70" r="396" fill="var(--paper)"/>
    <circle cx="705" cy="60" r="390" fill="url(#photoTone)" role="img" aria-label="Photo of a mother holding her newborn baby close"/>
    <path d="M340 1160 Q520 1000 827 985 L827 1160 Z" fill="var(--green)"/>
  </svg>

  <div class="brand">
    <div class="brand-mark"></div>
    <div class="brand-name">Wattle Grove<br>Health &amp;<br>Medical</div>
  </div>

  <h1 class="title">
    <span class="title-light">Cradle</span>
    <span class="title-bold">Ahead</span>
  </h1>
  <div class="cost">Cost:.................................</div>

  <div class="tab tab-left" style="top:345px">Week 1</div>
  <div class="copy" style="left:28px; top:400px; width:350px">
    <p style="padding-left:12px">GP Dr Elise Harmon will share information for Mum’s own health after delivery. Topics include:</p>
    <ul class="topics">
      <li>Vaccinations in pregnancy</li>
      <li>Bleeding, bladder and bowel after delivery</li>
      <li>Breastfeeding, engorgement and mastitis</li>
      <li>Bottle feeding</li>
      <li>Post-natal anxiety &amp; depression</li>
      <li>Intimacy and contraception</li>
    </ul>
  </div>

  <div class="tab tab-left" style="top:552px">Week 2</div>
  <div class="copy justify" style="left:24px; top:605px; width:350px">
    <p>Session 1 – Clinical Psychologist Dr Nadia Brooks will discuss changes in relationships as couples becomes parents, gender roles in parenting and post-natal depression.</p>
    <p>Session 2 – Physiotherapist Mara Whitfield will present advice for Mums regarding exercise during and after pregnancy, looking after the pelvic floor during and after pregnancy, and abdominal muscle separation management. She will also provide advice for promoting babies’ neck strength and minimising the risk of flat spots on the head and encouraging gross motor skills in the first 6 months</p>
  </div>

  <div class="tab tab-left" style="top:829px; padding-left:12px">Week 3</div>
  <div class="copy justify" style="left:22px; top:887px; width:362px">
    <p>Session 1 – Dietician Tessa Lowell provides advice for Mums regarding healthy eating during pregnancy and lactation, normal weight gain during pregnancy and realistic weight loss after. She will also discuss the evidence regarding breastfeeding VS bottle-feeding, normal infant weight gain and introducing solids (including those with potential for allergy).</p>
    <p>Session 2 – Paediatric Speech Pathologist Ruth Calder will share information about latching and breast-feeding troubles &amp; tongue tie, advice about dummies and finger-sucking, introducing solids &amp; feeding (including ‘pouch’ food), encouraging language development and current evidence about electronic devices impacting language development.</p>
  </div>

  <div class="tab tab-right" style="top:462px">Week 4</div>
  <div class="copy right" style="right:26px; top:516px; width:420px">
    <p>GP Dr Elise Harmon will share advice about your babies’ health in the first 6 months, including:</p>
    <ul class="topics align-right">
      <li>Skin of newborns</li>
      <li>Sleeping</li>
      <li>Crying</li>
      <li>Immunisations</li>
      <li>Fever and infections</li>
      <li>Diarrhoea and constipation</li>
      <li>Teething</li>
      <li>Understanding a baby’s signals</li>
    </ul>
  </div>

  <div class="tab tab-right" style="top:689px">Week 5</div>
  <div class="copy justify" style="left:443px; top:745px; width:360px; text-align-last:right">
    <p>Session 1 – Clinical Psychologist Dr Nadia Brooks will share information about bonding &amp; attachment with your baby, how to promote their social &amp; emotional development and how to manage separation anxiety. She will also discuss positive parenting approaches.</p>
  </div>

  <div class="tab tab-right" style="top:839px">Week 6</div>
  <div class="copy justify" style="left:446px; top:895px; width:360px; text-align-last:right">
    <p>Session 1 – Secret Men’s Business – a men-only session (including beer!) with a new father for frank discussion about the road ahead. Mums will do a shopping excursion with the GP &amp; Dietician to Freshway to look at baby products and food – the good and the bad!</p>
    <p>Session 2 - Program review, reflection and evaluation and future session planning when baby is 6 months of age.</p>
  </div>

  <address class="contact" style="font-style:normal">
    <div class="contact-line">02 5550 1234
      <svg viewBox="0 0 12 12"><path d="M3 1 L5 3.5 L4 5 Q5 7 7 8 L8.5 7 L11 9 L9.5 11 Q4 10.5 1 3 Z" fill="#fff"/></svg></div>
    <div class="contact-line">www.wattlegrovehealth.com.au
      <svg viewBox="0 0 12 12"><circle cx="6" cy="6" r="4.8" fill="none" stroke="#fff" stroke-width="1.3"/><path d="M1.5 6 H10.5 M6 1.2 V10.8" stroke="#fff" stroke-width="1"/></svg></div>
    <div class="contact-line">reception@wattlegrovehealth.com.au
      <svg viewBox="0 0 12 12"><rect x="1" y="2.5" width="10" height="7" fill="none" stroke="#fff" stroke-width="1.3"/><path d="M1 2.5 L6 6.5 L11 2.5" fill="none" stroke="#fff" stroke-width="1.2"/></svg></div>
    <div class="contact-line">Kestrel Bay Shopping Village, Shop 11
      <svg viewBox="0 0 12 12"><path d="M6 11.5 L2.5 6 A3.8 3.8 0 1 1 9.5 6 Z" fill="#fff"/><circle cx="6" cy="4.3" r="1.4" fill="var(--green)"/></svg></div>
    <div class="contact-line no-icon">482 Kestrel Way Kestrel Bay NSW 2999</div>
  </address>
</main>
</body>
</html>
```